We would like to incorporate our logo into letterhead design and envelopes. We are looking for something that is moderately conservative but not old law firm style. Both the envelopes and the letterhead must have both firm addresses. We would like to incorporate the color of the logo, but only a small amount of color - perhaps on one of the borders. The addresses for the firm locations are listed below. Given that it is a law firm, it needs to somewhat conservative, but not the old school, small black font on cream colored paper design.

The firm addresses are:

27815 N. Harlow Pemberton Pkwy.
Ste 4200
Scottsdale, AZ 85391

6100 W. Cedar Avenue
Ste 700
Burbank, CA 91623

Industry/Entity Type

Legal

Colors

Designer to choose colors to be used in the design.

Requirements
Must have
• Both addresses:
• 27815 N. Harlow Pemberton Pkwy.
• Ste 4200
• Scottsdale, AZ 85391
• 6100 W. Cedar Avenue
• Ste 700
• Burbank, CA 91623
Nice to have
• Small amount of color on border(s) that matches the logo but not too much color

```html
<!DOCTYPE html>
<html lang="en">
<head>
<meta charset="utf-8">
<title>Calloway Law Stationery</title>
<link href="https://fonts.googleapis.com/css2?family=Montserrat:wght@400;500&display=swap" rel="stylesheet">
<style>
  :root {
    --ink-brand: #3b3769;
    --paper: #efefef;
    --backdrop: #f4f2f0;
    --body-text: #8a8a94;
    --dark-text: #4a4a52;
    --heading-text: #2f2b66;
    --white: #ffffff;
  }
  * { margin: 0; padding: 0; box-sizing: border-box; }
  html, body {
    width: 1200px; height: 931px; overflow: hidden;
    background: var(--backdrop);
    font-family: "Montserrat", Arial, sans-serif;
  }
  .canvas { position: relative; width: 1200px; height: 931px; }

  .letterhead {
    position: absolute; left: 188px; top: 191px; width: 386px; height: 546px;
    background: var(--paper);
  }
  .brand-band {
    background: var(--ink-brand);
    display: flex; align-items: center; justify-content: center;
  }
  .letterhead .brand-band { height: 78px; }
  .brand-name {
    color: var(--white); font-weight: 400; letter-spacing: 0.06em;
    white-space: nowrap;
  }
  .letterhead .brand-name { font-size: 34px; }

  .letter-body { position: absolute; left: 29px; top: 148px; width: 330px; }
  .salutation { font-size: 8.8px; color: var(--heading-text); margin-bottom: 19px; }
  .paragraph {
    font-size: 7px; line-height: 10px; color: var(--body-text);
    margin-bottom: 12px;
  }
  .sign-off { font-size: 8.8px; color: var(--heading-text); margin-top: 12px; }
  .signer-name { font-size: 8.3px; color: var(--dark-text); margin-top: 7px; }
  .signer-title { font-size: 6px; color: var(--body-text); margin-top: 1px; }

  .address-block {
    position: absolute; left: 0; right: 0; text-align: center;
    font-size: 8.2px; line-height: 11.5px; color: var(--dark-text);
  }
  .letterhead .address-block { top: 509px; }

  .envelope-front {
    position: absolute; left: 611px; top: 299px; width: 405px; height: 202px;
    background: var(--paper);
  }
  .envelope-front .brand-band { height: 48px; }
  .envelope-front .brand-name, .envelope-back .brand-name { font-size: 21px; }
  .envelope-front .address-block { top: 170px; font-size: 7.8px; }

  .envelope-back {
    position: absolute; left: 609px; top: 533px; width: 405px; height: 204px;
    background: var(--ink-brand);
  }
  .envelope-flap { position: absolute; left: 0; top: 0; }
  .envelope-back .brand-band {
    position: absolute; left: 0; top: 0; width: 405px; height: 57px;
    background: transparent;
  }
</style>
</head>
<body>
<div class="canvas">

  <section class="letterhead">
    <header class="brand-band"><span class="brand-name">CALLOWAY LAW</span></header>
    <div class="letter-body">
      <p class="salutation">Dear sir/Madam,</p>
      <p class="paragraph">Lorem ipsum dolor sit amet, an vel recteque dissentiet, detracto albucius platonem ex vel, eros repudiandae cu. Atqui aliquando nec an, unum graece adolescens vel ad. Id odio scae has, iudico euismod atomorum ius ea, cum ea honestatis quaerendum theophrastus. Mea honestatis quaerendum theophrastus. Mea</p>
      <p class="paragraph">Lorem ipsum dolor sit amet, an vel recteque dissentiet, detracto albucius platonem ex vel, eros repudiandae cu. Atqui aliquando nec an, unum graece adolescens vel ad. Id odio scae has, iudico euismod atomorum ius ea, cum ea honestatis quaerendum theophrastus. Mea doming repudiandae ex, cu cum civibus assentior posidonium. Quo etiam pertinax ex, te eros repudiandae cu. Atqui aliquando nec an, unum graece adolescens vel ad. Id odio scae honestatis quaerendum theophrastus. Mea</p>
      <p class="paragraph">Lorem ipsum dolor sit amet, an vel recteque dissentiet, detracto albucius platonem ex vel, eros repudiandae cu. Atqui aliquando nec an, unum graece adolescens vel ad. Id odio scae has, iudico euismod atomorum ius ea, cum ea honestatis quaerendum theophrastus. Mea honestatis quaerendum theophrastus. Mea</p>
      <p class="paragraph">eros repudiandae cu. Atqui aliquando nec an, unum graece adolescens vel ad. Id odio scae honestatis quaerendum theophrastus. Mea posidonium. Quo etiam pertinax ex, te etiam pertinax ex, te</p>
      <p class="sign-off">Kind Regards</p>
      <p class="signer-name">Daniel R. Whitfield</p>
      <p class="signer-title">CEO / Founder</p>
    </div>
    <address class="address-block" style="font-style:normal">
      27815 N. Harlow Pemberton Pkwy. Ste 4200 Scottsdale, AZ 85391<br>
      6100 W. Cedar Avenue Ste 700 Burbank, CA 91623
    </address>
  </section>

  <section class="envelope-front">
    <header class="brand-band"><span class="brand-name">CALLOWAY LAW</span></header>
    <address class="address-block" style="font-style:normal">
      27815 N. Harlow Pemberton Pkwy. Ste 4200 Scottsdale, AZ 85391<br>
      6100 W. Cedar Avenue Ste 700 Burbank, CA 91623
    </address>
  </section>

  <section class="envelope-back">
    <svg class="envelope-flap" width="405" height="60" viewBox="0 0 405 60">
      <path d="M1 0 V50 Q1 57 9 57 H396 Q404 57 404 50 V0" fill="none" stroke="#4a4678" stroke-width="1"/>
    </svg>
    <div class="brand-band"><span class="brand-name">CALLOWAY LAW</span></div>
  </section>

</div>
</body>
</html>
```